Web site for small printshop

I am looking for a website for small printshop in Iceland, mainly serving university students and artist.

We print posters, flyers, business cards and more.

In addition to our current website, I would like to include design tool, (fx. www.quarvelink.com, www.tandorizo.com or something similar) jobs upload, shopping chart.
Updates

Great work, I am really amazed of the quality of work i am seeing here.

Really way beyond my expectation

GOOD JOB - all of you ! 

Hi all.

The designs submitted have been great, way better than expected.
I really did not expect this level of quality.

Some have been asking me for feedback on their designs, and I will try 
to send some feedback here, without spoiling your creativity.

Likes:
- when the colors of my logo is used in menus, buttons etc.
- simple, not to crowded look.

Dislikes.
- Dark and heavy design
- Lot of text and buttons (crowded look)

Extra info.
- top line (before menus) will contain: Tel - email - language
- menu line will have 5 categories: Home - service - submission of works - FAQ - about us
- 3 large buttons:  Job submit - Job design - ask for offer

LOVE YOUR WORK - great designs so far :)

Target Market(s)

University Students, Artists. Age group 20-30

Industry/Entity Type

University

Requirements
Must have
• The website must be easy to use, clean looking.

```html
<!DOCTYPE html>
<html lang="en">
<head>
<meta charset="utf-8">
<title>Lindaverk</title>
<link rel="stylesheet" href="https://fonts.googleapis.com/css2?family=Montserrat:wght@400;600;700&family=Oswald:wght@500&display=swap">
<style>
:root{
  --red:#e0352d;
  --red-dark:#c8221c;
  --green:#0f6b35;
  --green-dark:#0a5a2b;
  --ink:#222222;
  --text:#4a4a4a;
  --icon:#5f5f5f;
  --rule:#dcdcdc;
  --page:#efece3;
  --panel:#ffffff;
  --footer:#ededed;
}
*{box-sizing:border-box;margin:0;padding:0}
html,body{width:954px;height:1200px;overflow:hidden}
body{background:var(--page);font-family:"Montserrat",Arial,sans-serif;color:var(--text);position:relative}
.site-header{position:absolute;left:0;top:0;width:954px;height:67px;background:#fff}
.brand{position:absolute;left:111px;top:0;height:67px;display:flex;align-items:center}
.brand-name{font-weight:600;font-size:26px;color:var(--ink)}
.main-nav{position:absolute;left:455px;top:0;display:flex;height:67px}
.main-nav a{display:block;line-height:67px;padding:0 6px;font-size:11.6px;color:#333;text-decoration:none;white-space:nowrap}
.main-nav a.active{background:var(--red);color:#fff;width:48px;text-align:center;padding:0;margin-right:2px}
.hero{position:absolute;left:8px;top:67px;width:946px;height:320px;
  background:linear-gradient(90deg,#4c4640 0%,#6a6058 35%,#8a8580 62%,#cfcfcf 63%,#e6e6e6 100%)}
.panel{position:absolute;left:112px;top:372px;width:730px;height:815px;background:var(--panel);box-shadow:0 0 3px rgba(0,0,0,.15)}
.cta{position:absolute;top:15px;height:52px;width:345px;color:#fff;font-weight:700;font-size:18.5px;letter-spacing:.6px;line-height:52px;padding-left:15px}
.cta svg{position:absolute;right:18px;top:15px}
.cta-submit{left:15px;background:linear-gradient(var(--green),var(--green-dark))}
.cta-print{left:370px;background:linear-gradient(var(--red),var(--red-dark))}
.service{position:absolute;top:100px;width:167px}
.service h3{font-size:14.5px;font-weight:600;color:var(--ink);padding-bottom:10px;border-bottom:1px solid var(--rule)}
.service svg{display:block;margin:25px auto 0}
.service p{position:absolute;top:157px;left:0;width:170px;font-size:9.9px;letter-spacing:-.25px;line-height:17.2px;color:var(--text)}
.about{position:absolute;left:15px;top:440px;width:700px}
.about h2{font-size:19px;font-weight:700;color:var(--red)}
.about-text{position:absolute;top:44px;width:482px}
.about-text p{font-size:9.7px;letter-spacing:-.25px;line-height:17.2px;color:#333;margin-bottom:17px}
.location-map{position:absolute;left:495px;top:44px;width:205px;height:160px;background:linear-gradient(135deg,#d4d4d4,#bcbcbc)}
.site-footer{position:absolute;left:0;top:698px;width:730px;height:117px;background:var(--footer)}
.footer-col{position:absolute;top:18px}
.footer-col h4{font-family:"Oswald",Arial,sans-serif;font-weight:500;font-size:13px;color:#333;margin-bottom:8px;letter-spacing:.2px}
.footer-col p{font-size:10px;line-height:16px;color:#555}
.social{position:absolute;top:16px;right:16px;display:flex;gap:12px;align-items:center}
.social span{display:flex;align-items:center;gap:7px;font-family:"Oswald",Arial,sans-serif;font-weight:500;font-size:13px;color:#555}
.social i{display:block;width:26px;height:26px;border-radius:50%;background:#c9c9c9}
.copyright{position:absolute;right:16px;bottom:13px;font-size:9.4px;color:#444}
</style>
</head>
<body>
<header class="site-header">
  <div class="brand"><span class="brand-name">Lindaverk</span></div>
  <nav class="main-nav">
    <a class="active" href="#">Home</a>
    <a href="#">Services</a>
    <a href="#">Submission of Works</a>
    <a href="#">University Printing</a>
    <a href="#">Contact</a>
  </nav>
</header>

<div class="hero" role="img" aria-label="Wooden letterpress letters with printed book covers, and a smiling printer holding a printed sheet"></div>

<main class="panel">
  <a class="cta cta-submit">SUBMISSION OF WORKS<svg width="14" height="22" viewBox="0 0 14 22"><path d="M0 0L14 11L0 22Z" fill="#fff"/></svg></a>
  <a class="cta cta-print">UNIVERSITY PRINTING<svg width="14" height="22" viewBox="0 0 14 22"><path d="M0 0L14 11L0 22Z" fill="#fff"/></svg></a>

  <section class="service" style="left:14px">
    <h3>Photocopying</h3>
    <svg width="76" height="72" viewBox="0 0 76 72">
      <rect x="6" y="12" width="56" height="46" fill="var(--icon)" transform="rotate(-12 34 35)"/>
      <rect x="14" y="18" width="58" height="48" fill="var(--icon)" stroke="#fff" stroke-width="3" transform="rotate(12 43 42)"/>
      <rect x="22" y="26" width="42" height="32" fill="#fff" transform="rotate(12 43 42)"/>
      <path d="M26 52L36 40L44 48L50 42L60 54Z" fill="var(--icon)" transform="rotate(12 43 42)"/>
    </svg>
    <p>Duplicating Linda Copy Studio possesses one of the most powerful equipment in Iceland for photocopying. but we provide all generic copy in color or black and white, in small or large quantities</p>
  </section>

  <section class="service" style="left:191px">
    <h3>Printing</h3>
    <svg width="66" height="70" viewBox="0 0 66 70">
      <path d="M0 6L20 0V64L0 70Z M22 0L44 6V70L22 64Z M46 6L66 0V64L46 70Z" fill="var(--icon)"/>
    </svg>
    <p>We can print, brochures, invitations, business cards, newsletters, accounts or just anything you can think of. If we do not have the solution, we are in partnership with a number of companies that help us to deliver projects quickly and easily.</p>
  </section>

  <section class="service" style="left:369px">
    <h3>Book publishing</h3>
    <svg width="66" height="70" viewBox="0 0 66 70">
      <rect x="6" y="2" width="50" height="66" rx="5" fill="var(--icon)"/>
      <rect x="57" y="12" width="5" height="8" fill="var(--icon)"/><rect x="57" y="24" width="5" height="8" fill="var(--icon)"/><rect x="57" y="36" width="5" height="8" fill="var(--icon)"/>
      <g fill="#fff"><rect x="2" y="12" width="8" height="3"/><rect x="2" y="22" width="8" height="3"/><rect x="2" y="32" width="8" height="3"/><rect x="2" y="42" width="8" height="3"/><rect x="2" y="52" width="8" height="3"/>
      <circle cx="32" cy="26" r="6"/><path d="M21 46Q32 28 43 46Z"/></g>
    </svg>
    <p>We can print all kinds of books, but we have powerful equipment to print and bind the books, in quantities as desired. No quantity is too small or too big.</p>
  </section>

  <section class="service" style="left:547px">
    <h3>Scanning</h3>
    <svg width="64" height="90" viewBox="0 0 64 90" style="margin-top:18px">
      <rect x="31" y="0" width="2" height="90" fill="var(--icon)"/>
      <rect x="1" y="14" width="62" height="62" fill="var(--icon)"/>
      <rect x="8" y="21" width="48" height="36" fill="#fff"/>
      <rect x="32" y="21" width="24" height="36" fill="#bdbdbd"/>
      <path d="M10 55L24 38L34 48L42 40L54 55Z" fill="var(--icon)"/>
    </svg>
    <p>Lindaverk has more than 10 years experience in the scan. We have specialized scanners and can deliver content in a way that works best, but we can scan into TIF, JPG, PDF, PDF / A, Word, Exel, txt etc.</p>
  </section>

  <section class="about">
    <h2>Lindaverk / Lindafjölritun</h2>
    <div class="about-text">
      <p>Lindaverk er fyrirtæki staðsett á háskólasvæðinu sem hefur sérhæft sig í að þjónusta skólafólk, ásamt því að sinna allri almennri prentun fyrir almenning.</p>
      <p>Lindaverk er umhverfisvottuð prentsmiðja, en Laufið er opinbert umhverfismerki á Norðurlöndum, sem hefur skapað sér fótfestu hér á landi og er þekkt meðal neytenda.</p>
      <p>Lindaverk gefur út greinasöfn og frumsamdar kennslubækur fyrir námskeið, vinnur lokaritgerðir fyrir nema, auk þess að vinna við ótalinn fjölda smærri verka fyrir nemendur, kennara og stofnanir. Má þar nefna bæklinga, ritgerðir, bækur, OCR skönnun og fleira.</p>
    </div>
    <div class="location-map" role="img" aria-label="Street map showing the shop location on campus"></div>
  </section>

  <footer class="site-footer">
    <div class="footer-col" style="left:18px"><h4>SAY HELLO</h4><p>E: verk@lindaverk.is<br>T: 555 0147</p></div>
    <div class="footer-col" style="left:158px"><h4>ADDRESS</h4><p>Linda Copy Studio /<br>Lindaverk,<br>Sólvangsgötu 4,<br>105 Reykjavik</p></div>
    <div class="footer-col" style="left:300px"><h4>OPENING HOURS</h4><p>Mon - Fri: 9-17<br>closed on weekends</p></div>
    <div class="social"><span><i></i>CHIRPLY</span><span><i></i>FRIENDSTEAD</span></div>
    <p class="copyright">Copyright © 2013 Lindaverk. All rights reserved.</p>
  </footer>
</main>
</body>
</html>
```